Improve the existing label for Zentroluxiva company.

The ZLV company is launching a new product and needs the label for the product to be re-designed. Candidates should maintain the actual texts, and see if they can improve on the PuraVetrix Logo and the Biodegradable logo.
For the PuraVetrix Logo please use a diamond (any diamont will suffice)
The label should maintain the blue on white aspect and can use blue gradients.(monochromatic).
the white part of the label and the bottle will be transparent, and the liquid inside the bottle is blue.

The product is a monitor/tv/cell/tablet screen cleaner.
The label size is (7 cm in heigh)t and (3,8 cm in lenght).

The actual label is attached.

Thanks in advance for your designs.

```html
<!DOCTYPE html>
<html lang="pt">
<head>
<meta charset="utf-8">
<title>PuraVetrix – Linha Clara</title>
<link rel="stylesheet" href="https://fonts.googleapis.com/css2?family=Arimo:ital,wght@0,700;1,700&display=swap">
<style>
  :root {
    --ink: #3d1578;
    --frame: #48197f;
    --badge: #4b1c86;
    --paper: #ffffff;
  }
  * { margin: 0; padding: 0; box-sizing: border-box; }
  html, body {
    width: 1200px;
    height: 900px;
    overflow: hidden;
    background: var(--paper);
  }
  .canvas {
    position: relative;
    width: 1200px;
    height: 900px;
    font-family: "Arimo", Arial, sans-serif;
    color: var(--ink);
  }
  .label {
    position: absolute;
    left: 193px;
    top: 97px;
    width: 384px;
    height: 709px;
    border: 5px solid var(--frame);
    border-radius: 22px;
    background: var(--paper);
    text-align: center;
  }
  .brand {
    position: absolute;
    top: 74px;
    left: 0;
    right: 0;
    font-weight: 700;
    font-size: 46px;
    line-height: 1;
    letter-spacing: 0.5px;
    text-transform: uppercase;
  }
  .product-line {
    position: absolute;
    top: 177px;
    left: 0;
    right: 0;
    font-weight: 700;
    font-style: italic;
    font-size: 27px;
  }
  .usage {
    position: absolute;
    top: 251px;
    left: 0;
    right: 0;
    font-weight: 700;
    font-size: 28.7px;
    line-height: 35.7px;
    text-transform: uppercase;
    white-space: nowrap;
  }
  .eco-seal {
    position: absolute;
    top: 458px;
    left: 109px;
    width: 156px;
    height: 156px;
  }
  .volume {
    position: absolute;
    top: 651px;
    left: 0;
    right: 0;
    font-weight: 700;
    font-style: italic;
    font-size: 21px;
  }
</style>
</head>
<body>
<main class="canvas">
  <section class="label">
    <h1 class="brand">PuraVetrix</h1>
    <p class="product-line">Linha Clara</p>
    <p class="usage">
      Para limpeza de<br>
      monitores - TV - LCD<br>
      LED - plasma - óculos<br>
      cameras - tablets<br>
      celulares
    </p>
    <svg class="eco-seal" viewBox="0 0 156 156" aria-hidden="true">
      <circle cx="78" cy="78" r="78" fill="var(--badge)"/>
    </svg>
    <p class="volume">CONTÉM 60 ml</p>
  </section>
</main>
</body>
</html>
```